Postcard Design

I'm hosting a retreat in Tuscany tag line ideas for front: "nourish your soul with a taste of Tuscany" or "Savor the sweet life and Nourish your soul with a taste of Tuscany" here is the pertinent info- trip date: September 5-12, 2015 number:1.877.413.5928 e/m:Info@PiccoloSoleHavens.com Web address:www.PiccoloSoleHavens.com
What's included:
• 7 nights Accommodations in beautiful Villa
• All Meals and Snacks included
• Special Wine tasting Excursion in Chianti
• Guided Tour of Siena
• Hands on Cooking Class at the villa
• Yoga, Meditation walks, Journaling
Something like this should be on back lower right side: Spaces Limited Reserve Yours Today!
Other wording ideas for back: Renew your spirit in the quiet beauty of the Tuscan landscape (maybe above what's included)
This can be near the "spaces limited" =Invest in your health, spirit and well-being *airfare not included. See website for details
More ideas/maybe a better way to word all this??:
Welcome to "la dolce vita" (The sweet life)
Have you always wanted to travel to Italy? Want to experience the culture in a special way you couldn't enjoy as a typical tourist? This is the trip you've been waiting for. Life is too short to wait any longer!
Hosts show with pictures:
Lucy Jane Ferrandi woman w/dark hair headshot
Retreat host
Sharing her love of Italy's beautiful culture with you is her special gift
And
Megan Okabashi
Personal wellness consultant
Yoga, Meditation, Asana, Reiki, Pilates

I included a photo of the current postcard I made front & back. You can also visit my website to get an idea of my style. I'm hoping you can make me a postcard that's more tantalizing, and will get me some clients! I will include some extra photos and feel free to use your own stock images... anything to help! Feel free to change up wording to make it more appealing, welcoming and make people chose to go on retreat with me instead the hundreds of other retreats out there.
Thank you
Lucy Jane

```html
<!DOCTYPE html>
<html lang="en">
<head>
<meta charset="utf-8">
<title>Piccolo Sole Havens – Tuscany Retreat Postcard</title>
<link rel="stylesheet" href="https://fonts.googleapis.com/css2?family=Quicksand:wght@400;500&family=Pinyon+Script&display=swap">
<style>
  :root {
    --page: #e6e3de;
    --paper: #f7f4ec;
    --paper-edge: #ece6d6;
    --band: #5b4a2f;
    --band-text: #fbf6ea;
    --ink: #6b5a3f;
    --ink-soft: #7d6e56;
    --rule: #d9cfba;
    --line: #c9c6c0;
    --sky: #8fb3d6;
    --field: #a88d4a;
    --grass: #5f7f33;
    --tree: #3f5a2a;
    --sans: "Quicksand", "Century Gothic", sans-serif;
    --script: "Pinyon Script", cursive;
  }
  * { box-sizing: border-box; margin: 0; padding: 0; }
  html, body { width: 910px; height: 1200px; overflow: hidden; }
  body { background: var(--page); font-family: var(--sans); color: var(--ink); position: relative; }

  .postcard {
    position: absolute; width: 738px; height: 532px;
    background: radial-gradient(ellipse at 40% 60%, var(--paper) 60%, var(--paper-edge) 100%);
    box-shadow: 0 1px 3px rgba(0,0,0,.15);
  }
  .postcard--front { left: 70px; top: 58px; }
  .postcard--back { left: 122px; top: 624px; }

  .photo { position: absolute; }
  .photo--villa {
    left: 0; top: 0; width: 513px; height: 320px;
    background: linear-gradient(180deg, var(--sky) 0%, #cfe0ee 28%, var(--tree) 34%, var(--field) 45%, #b99a55 55%, var(--grass) 68%, #4d6f2a 100%);
  }
  .photo--table {
    left: 463px; top: 292px; width: 275px; height: 175px;
    border: 2px solid #fff; outline: 1px solid #333;
    background: linear-gradient(180deg, #c7d9e8 0%, #dfe7ea 30%, #6e8b3d 45%, #51702c 62%, #47473f 75%, #6a6a64 100%);
  }

  .side-panel { position: absolute; left: 515px; top: 0; width: 223px; height: 290px; border-left: 2px solid #222; text-align: center; }
  .brand {
    margin: 40px auto 0; width: 196px; height: 58px;
    display: flex; align-items: center; justify-content: center; gap: 8px;
    font-family: var(--sans); font-weight: 500; font-size: 17px; color: #2e2a24;
  }
  .brand__mark { width: 10px; height: 10px; border-radius: 50%; background: #2e2a24; }
  .invite { margin-top: 12px; font-size: 12.5px; line-height: 18px; color: var(--ink-soft); }
  .motto { margin-top: 22px; font-size: 12.5px; line-height: 17px; text-transform: uppercase; color: var(--ink-soft); }
  .trip-date { margin-top: 18px; font-size: 18px; color: var(--ink-soft); }

  .band {
    position: absolute; background: var(--band); color: var(--band-text);
    font-family: var(--script); font-size: 30px; line-height: 30px;
  }
  .band--front { left: 0; top: 319px; width: 493px; height: 74px; padding: 6px 0 0 45px; }
  .band--front span { display: block; }
  .band--front span + span { padding-left: 32px; }
  .band--back { left: 0; top: 259px; width: 478px; height: 72px; padding: 8px 0 0 30px; }
  .band--back span { display: block; }
  .band--back span + span { padding-left: 205px; }

  .included { position: absolute; left: 23px; top: 402px; font-size: 11px; line-height: 16px; color: var(--ink-soft); }
  .included__title { margin-bottom: 3px; }
  .included__lists { display: flex; gap: 20px; }
  .included ul { list-style: none; }
  .included li::before { content: "• "; }

  .contact-row {
    position: absolute; left: 0; right: 0; display: flex; align-items: center; justify-content: center;
    gap: 34px; font-size: 12.5px; color: var(--ink-soft);
  }
  .contact-row::before, .contact-row::after { content: ""; position: absolute; top: 50%; height: 3px; width: 72px; background: var(--rule); }
  .contact-row::before { left: 0; } .contact-row::after { right: 0; }
  .postcard--front .contact-row { top: 494px; }
  .postcard--back .contact-row { top: 491px; left: 0; right: 0; }
  .contact { display: flex; align-items: center; gap: 6px; }
  .contact svg { width: 16px; height: 16px; }

  .pitch { position: absolute; left: 0; width: 478px; top: 18px; text-align: center; font-size: 13px; line-height: 16px; color: var(--ink-soft); }
  .pitch p + p { margin-top: 6px; }

  .photo-strip { position: absolute; left: 0; top: 126px; width: 464px; height: 133px; display: flex; }
  .photo-strip .photo { position: relative; height: 100%; border: 1px solid #fff; }
  .photo--spa { width: 154px; background: linear-gradient(180deg, #bcd3e5 0%, #5e7d34 35%, #4f6f2b 65%, #7a5e3d 100%); }
  .photo--patio { width: 155px; background: linear-gradient(180deg, #6b7d45 0%, #8c7a52 40%, #e9e6df 62%, #b24a3c 80%, #e4e1da 100%); }
  .photo--pool { width: 155px; background: linear-gradient(180deg, #c8dcec 0%, #4e6e2c 30%, #b79e60 50%, #6e8c3a 65%, #79b5cf 82%, #5b4a2f 100%); }

  .hosts { position: absolute; left: 22px; top: 342px; display: flex; gap: 10px; }
  .host { width: 190px; text-align: center; font-size: 12px; line-height: 17px; color: var(--ink-soft); }
  .host .photo { position: relative; margin: 0 auto 6px; width: 98px; height: 95px; border: 1px solid #222; }
  .photo--host-one { background: linear-gradient(180deg, #9ec3dc 0%, #6b9ac0 55%, #3e6b94 100%); }
  .photo--host-two { background: linear-gradient(180deg, #8c8a84 0%, #a3a09a 55%, #3b3633 100%); }

  .stamp { position: absolute; left: 556px; top: 20px; width: 165px; height: 80px; background: linear-gradient(90deg, #e3e1dc, #d6d4cf); opacity: .8; }
  .address-lines { position: absolute; left: 500px; top: 179px; width: 212px; }
  .address-lines span { display: block; height: 1px; background: var(--line); margin-bottom: 31px; }
</style>
</head>
<body>

<section class="postcard postcard--front" aria-label="Postcard front">
  <div class="photo photo--villa" role="img" aria-label="Tuscan stone villa with pool among golden fields and cypress trees"></div>

  <aside class="side-panel">
    <div class="brand"><span class="brand__mark"></span>Piccolo Sole Havens</div>
    <p class="invite">Come have a love affair with Italy<br>and the beguiling beauty of Tuscany</p>
    <p class="motto">Savor the sweet life<br>living la dolce vita</p>
    <p class="trip-date">September 5-12, 2015</p>
  </aside>

  <div class="photo photo--table" role="img" aria-label="Outdoor dinner table with wine overlooking green Tuscan hills"></div>

  <h2 class="band band--front"><span>nourish your soul</span><span>with a taste of Tuscany</span></h2>

  <div class="included">
    <p class="included__title">What's included:</p>
    <div class="included__lists">
      <ul>
        <li>7 nights Accommodations in beautiful Villa</li>
        <li>All Meals and Snacks included</li>
        <li>Special Wine tasting Excursion in Chianti</li>
      </ul>
      <ul>
        <li>Guided Tour of Siena</li>
        <li>Hands on Cooking Class at the villa</li>
        <li>Yoga, Meditation walks, Journaling</li>
      </ul>
    </div>
  </div>

  <div class="contact-row">
    <span class="contact"><svg viewBox="0 0 16 16" fill="none" stroke="#b3a88f" stroke-width="1.3"><rect x="1.5" y="4" width="13" height="9"/><path d="M1.5 4l6.5 5 6.5-5"/></svg>Info@PiccoloSoleHavens.com</span>
    <span class="contact"><svg viewBox="0 0 16 16" fill="#b3a88f"><path d="M4 1.5l2.5 3-1.5 1.8c.8 1.8 2 3 3.8 3.8L10.6 8.5l3 2.5-1.4 2.5C7 13 3 9 2.5 3z"/></svg>1.877.413.5928</span>
    <span class="contact"><svg viewBox="0 0 16 16" fill="none" stroke="#b3a88f" stroke-width="1.3"><circle cx="8" cy="8" r="6.5"/><path d="M1.5 8h13M8 1.5c-3 3.5-3 9.5 0 13M8 1.5c3 3.5 3 9.5 0 13"/></svg>www.PiccoloSoleHavens.com</span>
  </div>
</section>

<section class="postcard postcard--back" aria-label="Postcard back">
  <div class="pitch">
    <p>Have you always wanted to travel to Italy?<br>Want to experience the culture in a special way you couldn't enjoy<br>as a typical tourist?</p>
    <p>This is the trip you've been waiting for.<br>Life is too short to wait any longer!</p>
  </div>

  <div class="stamp" role="img" aria-label="Stamp area with postmark"></div>

  <div class="photo-strip">
    <div class="photo photo--spa" role="img" aria-label="Garden hot tub on a wooden deck"></div>
    <div class="photo photo--patio" role="img" aria-label="Shaded patio table set for lunch"></div>
    <div class="photo photo--pool" role="img" aria-label="Villa swimming pool beside the fields"></div>
  </div>

  <h2 class="band band--back"><span>Welcome to "la Dolce Vita"</span><span>the sweet life</span></h2>

  <div class="address-lines"><span></span><span></span><span></span><span></span><span></span><span></span></div>

  <div class="hosts">
    <figure class="host">
      <div class="photo photo--host-one" role="img" aria-label="Headshot of retreat host Lucy Jane Ferrandi"></div>
      <figcaption>Lucy Jane Ferrandi<br>Retreat host, Event Planner, Italophile</figcaption>
    </figure>
    <figure class="host">
      <div class="photo photo--host-two" role="img" aria-label="Headshot of wellness consultant Megan Okabashi"></div>
      <figcaption>Megan Okabashi<br>Personal wellness consultant</figcaption>
    </figure>
  </div>

  <div class="contact-row">
    <span class="contact"><svg viewBox="0 0 16 16" fill="none" stroke="#b3a88f" stroke-width="1.3"><rect x="1.5" y="4" width="13" height="9"/><path d="M1.5 4l6.5 5 6.5-5"/></svg>Info@PiccoloSoleHavens.com</span>
    <span class="contact"><svg viewBox="0 0 16 16" fill="#b3a88f"><path d="M4 1.5l2.5 3-1.5 1.8c.8 1.8 2 3 3.8 3.8L10.6 8.5l3 2.5-1.4 2.5C7 13 3 9 2.5 3z"/></svg>1.877.413.5928</span>
    <span class="contact"><svg viewBox="0 0 16 16" fill="none" stroke="#b3a88f" stroke-width="1.3"><circle cx="8" cy="8" r="6.5"/><path d="M1.5 8h13M8 1.5c-3 3.5-3 9.5 0 13M8 1.5c3 3.5 3 9.5 0 13"/></svg>www.PiccoloSoleHavens.com</span>
  </div>
</section>

</body>
</html>
```